SkyRavelin Unique Gift Certificate

We need a unique, luxury gift certificate created for our online company (SkyRavelin). We are looking for something out of the ordinary, ie. do not want it to look like a 'normal' gift certificate. Please visit our website to gain a feel for our company (skyravelin.com.au). The dimensions are 148x148mm. We need our logo, website details, to, from, description, code, exp date included. The certificate will be printed on wood veneer so watermarks will not work. We want it to be clean and minimalistic.

Industry/Entity Type

It Company

```html
<!DOCTYPE html>
<html lang="en">
<head>
<meta charset="utf-8">
<title>SkyRavelin Gift Certificate</title>
<link rel="stylesheet" href="https://fonts.googleapis.com/css2?family=Cinzel:wght@400;700&family=Cormorant+Garamond:ital,wght@1,600&family=Roboto:wght@400&display=swap">
<style>
  :root {
    --stage-left: #ecebe8;
    --stage-right: #ffffff;
    --divider: #c9c9c9;
    --wood-light: #e4b985;
    --wood-dark: #d6a670;
    --teal: #3d8783;
    --teal-dark: #2f5f5c;
    --sky: #1fb4e2;
    --ink: #1b1a18;
    --rule: #3a3632;
    --muted: #5d5650;
    --paper: #ffffff;
  }
  * { margin: 0; padding: 0; box-sizing: border-box; }
  html, body { width: 1200px; height: 596px; overflow: hidden; }
  body { position: relative; background: var(--stage-right); }
  .stage-left {
    position: absolute; left: 0; top: 0; width: 608px; height: 596px;
    background: var(--stage-left); border-right: 2px solid var(--divider);
  }
  .certificate {
    position: absolute; top: 58px; width: 616px; height: 616px;
    transform: scale(0.8); transform-origin: top left;
    color: var(--ink);
  }
  .certificate--wood {
    left: 58px;
    background: linear-gradient(160deg, var(--wood-light), var(--wood-dark) 60%, var(--wood-light));
    box-shadow: 0 2px 6px rgba(0,0,0,.25);
    --frame: var(--teal); --frame-inner: var(--teal-dark); --web: var(--muted); --ornament: #6e5a44;
  }
  .certificate--white {
    left: 669px; background: var(--paper);
    box-shadow: 0 1px 5px rgba(0,0,0,.18);
    --frame: var(--sky); --frame-inner: var(--sky); --web: var(--sky); --ornament: #555;
  }
  .frame { position: absolute; inset: 0; }
  .abs { position: absolute; left: 0; width: 616px; text-align: center; }
  .title {
    top: 64px; font-family: "Cinzel", serif; font-weight: 700;
    font-size: 28px; letter-spacing: 1px; white-space: nowrap;
  }
  .ornament {
    position: absolute; left: 224px; top: 105px; width: 168px; height: 12px;
    background: var(--ornament); opacity: .55; border-radius: 6px;
  }
  .label {
    font-family: "Cormorant Garamond", serif; font-style: italic; font-weight: 600; font-size: 16px;
  }
  .awarded { top: 129px; }
  .from { top: 237px; }
  .name {
    font-family: "Cinzel", serif; font-weight: 400; font-size: 30px; letter-spacing: 1px;
  }
  .recipient { top: 165px; }
  .sender { top: 262px; }
  .description {
    top: 320px; left: 82px; width: 452px;
    font-family: "Cormorant Garamond", serif; font-style: italic; font-weight: 600;
    font-size: 11.6px; line-height: 16.5px;
  }
  .brand-mark {
    position: absolute; left: 258px; top: 432px; width: 102px; height: 102px;
    border-radius: 50%; border: 5px solid var(--frame); opacity: .85;
  }
  .brand-name {
    top: 546px; font-family: "Roboto", sans-serif; font-size: 15px; color: #3b3b3b;
  }
  .field { position: absolute; top: 548px; width: 143px; border-top: 1px solid var(--rule); }
  .field-number { left: 78px; }
  .field-date { left: 396px; }
  .field-label {
    position: absolute; top: 553px; font-family: "Cormorant Garamond", serif;
    font-style: italic; font-weight: 600; font-size: 12.5px; white-space: nowrap;
  }
  .field-label.number { left: 109px; }
  .field-label.date { left: 399px; }
  .website {
    top: 588px; font-family: "Roboto", sans-serif; font-size: 10px; color: var(--web);
  }
</style>
</head>
<body>
  <div class="stage-left"></div>

  <section class="certificate certificate--wood">
    <svg class="frame" width="616" height="616" viewBox="0 0 616 616" aria-hidden="true">
      <path d="M246 594.5H21.5V21.5H594.5V594.5H373" fill="none" stroke="var(--frame)" stroke-width="7"/>
      <path d="M246 587.5H28.5V28.5H587.5V587.5H373" fill="none" stroke="var(--frame-inner)" stroke-width="1.2"/>
      <line x1="65" y1="111" x2="222" y2="111" stroke="var(--rule)" stroke-width="1"/>
      <line x1="394" y1="111" x2="552" y2="111" stroke="var(--rule)" stroke-width="1"/>
      <line x1="91" y1="206" x2="526" y2="206" stroke="var(--rule)" stroke-width="1"/>
      <line x1="91" y1="303" x2="526" y2="303" stroke="var(--rule)" stroke-width="1"/>
    </svg>
    <h1 class="abs title">Certificate of Completion</h1>
    <div class="ornament" role="img" aria-label="Decorative flourish divider"></div>
    <p class="abs label awarded">Awarded to</p>
    <p class="abs name recipient">Lorem Ipsum</p>
    <p class="abs label from">From</p>
    <p class="abs name sender">Dolor Sit Amet</p>
    <p class="abs description">Lorem ipsum dolor sit amet, consectetur adipiscing elit. Morbi sagittis aliquam magna, vel scelerisque lectus sollicitudin sollicitudin. Duis ac arcu a leo molestie auctor. Ut sed magna ex, Proin sodales eget enim et viverra. Curabitur enim metus, euismod at consequat quis, pretium vel nunc. Aenean vel lacus in magna maximus hendrerit.</p>
    <div class="brand-mark"></div>
    <p class="abs brand-name">skyravelin</p>
    <div class="field field-number"></div>
    <div class="field field-date"></div>
    <p class="field-label number">Certificate Number</p>
    <p class="field-label date">Certificate Date : (Exp. 1 Years)</p>
    <p class="abs website">www.skyravelin.com.au</p>
  </section>

  <section class="certificate certificate--white">
    <svg class="frame" width="616" height="616" viewBox="0 0 616 616" aria-hidden="true">
      <path d="M246 594.5H21.5V21.5H594.5V594.5H373" fill="none" stroke="var(--frame)" stroke-width="7"/>
      <path d="M246 587.5H28.5V28.5H587.5V587.5H373" fill="none" stroke="var(--frame-inner)" stroke-width="1.5"/>
      <line x1="65" y1="111" x2="222" y2="111" stroke="var(--rule)" stroke-width="1"/>
      <line x1="394" y1="111" x2="552" y2="111" stroke="var(--rule)" stroke-width="1"/>
      <line x1="91" y1="206" x2="526" y2="206" stroke="var(--rule)" stroke-width="1"/>
      <line x1="91" y1="303" x2="526" y2="303" stroke="var(--rule)" stroke-width="1"/>
    </svg>
    <h1 class="abs title">Certificate of Completion</h1>
    <div class="ornament" role="img" aria-label="Decorative flourish divider"></div>
    <p class="abs label awarded">Awarded to</p>
    <p class="abs name recipient">Lorem Ipsum</p>
    <p class="abs label from">From</p>
    <p class="abs name sender">Dolor Sit Amet</p>
    <p class="abs description">Lorem ipsum dolor sit amet, consectetur adipiscing elit. Morbi sagittis aliquam magna, vel scelerisque lectus sollicitudin sollicitudin. Duis ac arcu a leo molestie auctor. Ut sed magna ex, Proin sodales eget enim et viverra. Curabitur enim metus, euismod at consequat quis, pretium vel nunc. Aenean vel lacus in magna maximus hendrerit.</p>
    <div class="brand-mark"></div>
    <p class="abs brand-name">skyravelin</p>
    <div class="field field-number"></div>
    <div class="field field-date"></div>
    <p class="field-label number">Certificate Number</p>
    <p class="field-label date">Certificate Date : (Exp. 1 Years)</p>
    <p class="abs website">www.skyravelin.com.au</p>
  </section>
</body>
</html>
```